Modern Homepage Design for brenvik.nl – Fish & Chicken Food Webshop

Brenvik.nl is an online store that sells fish and chicken food. The design should be visually appealing, easy to navigate, and optimized for e-commerce. We want a layout that helps customers quickly find what they need and encourages them to explore our products.
A good example of the style and structure we like is dierkamp.nl – clean layout, clear product focus, and user-friendly navigation.
Brand Colors (must be used):
Orange: #f7a441
Dark Gray: #3c3c3b
White: #ffffff
Please use these colors consistently throughout the design.
Homepage Requirements:
The homepage should include the following sections:
Main Slider / Hero Banner
A large, eye-catching slider at the top of the page to highlight promotions or featured categories.
Category Blocks
A section with clear, clickable blocks or tiles that link to main product categories (e.g., Fish Food, Chicken Food, Accessories).
Featured Products
A section showcasing selected or best-selling products.
Special Offers / Promotions
A space to highlight current deals or limited-time offers.
Three Banners in a Row
A section with three horizontal banners side by side, which can be used for promotions, shipping info, or other key messages.
Unique Selling Points (USPs)
A section that briefly explains what makes our store different (e.g., fast delivery, high-quality feed, trusted by professionals).
SEO Content Block
A short paragraph of text for SEO purposes (use Lorem Ipsum for dummy content).
Footer Design
Include space for contact information, navigation links, and social media.
Design Notes:
The design must be responsive and mobile-friendly.
Focus on clean layout, good spacing, and easy navigation.
Use modern fonts and a clear visual hierarchy.
We are only looking for the homepage design at this stage, but we may work with the selected designer on additional pages later.
Deliverables:
Homepage design in layered PSD, Figma, or Adobe XD format
Any fonts and assets used
Preview images/mockups
We look forward to seeing your ideas and working with a designer who can bring our brand to life with a fresh and functional homepage design.
Let us know if you have any questions.
Hobby Animal Keepers, Pet Owners
Animal Nutrition & Feed
2 page

```html
<!DOCTYPE html>
<html lang="en">
<head>
<meta charset="utf-8">
<title>Brenvik.nl – Fish &amp; Chicken Food</title>
<link href="https://fonts.googleapis.com/css2?family=Oswald:wght@400;500;600;700&family=Poppins:wght@400;500;600&display=swap" rel="stylesheet">
<style>
:root{
  --orange:#f7a441;
  --orange-deep:#f39a2e;
  --dark:#3c3c3b;
  --ink:#222221;
  --white:#ffffff;
  --peach:#fbe3c6;
  --cream:#fdf0df;
  --line:#e6e6e6;
  --muted:#6f6f6e;
}
*{box-sizing:border-box;margin:0;padding:0}
html,body{width:1200px;height:3528px;overflow:hidden}
body{position:relative;background:var(--white);font-family:"Poppins",sans-serif;color:var(--dark)}
.section{position:absolute;left:0;width:1200px}
.heading{font-family:"Oswald",sans-serif;font-weight:700;text-transform:uppercase;color:var(--ink)}
.btn{display:inline-flex;align-items:center;justify-content:center;border-radius:30px;font-family:"Poppins",sans-serif;font-weight:600;font-size:13px;text-transform:uppercase}
.btn-dark{background:var(--ink);color:var(--white)}
.btn-orange{background:var(--orange);color:var(--white)}
.media{position:absolute;border-radius:6px}

/* top bar */
.topbar{top:0;height:32px;background:var(--ink);color:var(--white);font-size:12px;display:flex;align-items:center;justify-content:center;gap:8px}
/* header */
.header{top:32px;height:120px}
.logo{position:absolute;left:158px;top:40px;display:flex;align-items:center;gap:8px;font-family:"Poppins",sans-serif;font-weight:600;font-size:32px;color:var(--dark)}
.logo-dot{width:30px;height:30px;border-radius:50%;background:var(--orange)}
.search{position:absolute;left:424px;top:44px;width:360px;height:34px;border:1px solid var(--line);border-radius:20px;display:flex;align-items:center;padding-left:14px;gap:8px;font-size:12px;color:#999}
.account{position:absolute;left:808px;top:44px;width:110px;height:34px;border:1px solid var(--dark);border-radius:20px;display:flex;align-items:center;justify-content:center;gap:8px;font-size:13px}
.cart{position:absolute;left:930px;top:44px;width:112px;height:34px;background:var(--orange);border-radius:20px;color:var(--white);display:flex;align-items:center;justify-content:center;gap:8px;font-size:13px;font-weight:600}
.nav{top:152px;height:32px;border-bottom:1px solid var(--line);display:flex;justify-content:center;gap:48px;align-items:center;font-size:12px;font-weight:500;text-transform:uppercase}
.nav a{color:var(--dark);text-decoration:none}
.nav a.active{color:var(--orange)}

/* hero */
.hero{top:184px;height:464px;background:var(--orange);overflow:hidden}
.hero-title{position:absolute;left:160px;top:96px;font-size:58px;line-height:1.08;color:var(--white)}
.hero-text{position:absolute;left:160px;top:240px;width:300px;font-size:13px;line-height:1.5;color:var(--white)}
.hero .btn{position:absolute;left:160px;top:322px;width:110px;height:32px}
.hero-media{left:560px;top:0;width:640px;height:464px;border-radius:0;background:linear-gradient(120deg,#f3b25f 0%,#7f6a4d 45%,#2e3437 100%)}
.slide-arrow{position:absolute;top:216px;width:34px;height:44px;background:rgba(60,60,59,.55);display:flex;align-items:center;justify-content:center}

/* categories */
.categories{top:700px;height:560px}
.section-title{position:absolute;left:0;width:1200px;text-align:center;font-size:36px}
.cat-card{position:absolute;top:132px;width:268px;height:256px;background:var(--white);border-radius:14px;box-shadow:0 6px 22px rgba(0,0,0,.12)}
.cat-card.accent{background:var(--orange)}
.cat-label{position:absolute;left:24px;top:24px;font-family:"Oswald",sans-serif;text-transform:uppercase;line-height:1}
.cat-label .small{display:block;font-size:30px;color:var(--ink);font-weight:500}
.cat-label .big{display:block;font-size:64px;color:var(--orange);font-weight:700}
.cat-card.accent .cat-label .small{color:var(--white);font-size:36px}
.cat-card.accent .cat-label .big{color:var(--white);font-size:36px}
.cat-media{left:60px;top:150px;width:180px;height:200px;border-radius:50%}

/* featured */
.featured{top:1220px;height:620px}
.product{position:absolute;top:92px;width:235px;height:400px;border:1px solid var(--line);border-radius:8px;background:var(--white);text-align:center}
.stars{margin-top:22px;font-size:13px;color:var(--orange);letter-spacing:2px}
.stars span{color:var(--muted);font-size:11px;letter-spacing:0}
.product-media{left:67px;top:56px;width:100px;height:150px}
.price{position:absolute;left:93px;top:228px;width:48px;height:18px;background:var(--orange);color:var(--white);font-size:10px;font-weight:600;border-radius:2px;display:flex;align-items:center;justify-content:center}
.product-name{position:absolute;left:0;width:100%;top:262px;font-family:"Oswald",sans-serif;font-weight:600;font-size:25px;color:var(--ink);white-space:nowrap}
.add-cart{position:absolute;left:47px;top:318px;width:140px;height:34px;border:1.5px solid var(--ink);border-radius:20px;font-size:12px;font-weight:600;display:flex;align-items:center;justify-content:center}
.dots{position:absolute;top:508px;left:0;width:1200px;display:flex;justify-content:center;gap:8px}
.dots i{width:7px;height:7px;border-radius:50%;background:#c9c9c9}
.dots i.on{background:var(--dark)}
.featured .view-all{position:absolute;left:514px;top:548px;width:172px;height:34px;font-size:11px}

/* deal */
.deal{top:1864px;height:400px;background:var(--peach);overflow:hidden}
.deal-title{position:absolute;left:160px;top:118px;font-size:66px;line-height:1.02;white-space:nowrap}
.deal-text{position:absolute;left:160px;top:202px;width:290px;font-size:13px;line-height:1.5;color:var(--dark)}
.deal .btn{position:absolute;left:160px;top:256px;width:120px;height:32px}
.deal-media{left:620px;top:0;width:580px;height:400px;border-radius:0;background:linear-gradient(110deg,rgba(251,227,198,0) 0%,#c77a34 25%,#3a3a36 70%,#1f2526 100%)}

/* promo banners */
.promos{top:2312px;height:176px}
.promo{position:absolute;top:0;width:344px;height:176px;background:var(--cream);border-radius:6px;overflow:hidden}
.promo-text{position:absolute;left:20px;top:46px;font-family:"Oswald",sans-serif;font-weight:700;text-transform:uppercase;font-size:26px;line-height:1.05;color:var(--ink)}
.promo-text .hl{display:block;color:var(--orange)}
.promo-side{position:absolute;right:0;top:0;width:150px;height:176px;background:var(--orange)}
.promo-media{right:40px;top:18px;width:110px;height:140px}
.promo-go{position:absolute;right:14px;bottom:16px;width:32px;height:32px;border-radius:50%;background:var(--ink);display:flex;align-items:center;justify-content:center}

/* why choose */
.why{top:2544px;height:320px}
.ribbon{position:absolute;left:248px;top:0;width:704px;height:304px}
.why-title{position:absolute;left:0;width:1200px;top:36px;text-align:center;font-size:38px;color:var(--white)}
.why-text{position:absolute;left:400px;width:400px;top:96px;text-align:center;font-size:13px;line-height:1.5;color:var(--white)}
.usp{position:absolute;top:164px;display:flex;align-items:center;gap:10px;font-family:"Oswald",sans-serif;font-weight:600;font-size:20px;color:var(--white);line-height:1.05}

/* seo */
.seo{top:2900px;height:320px}
.seo-title{top:10px;font-size:38px}
.seo-body{position:absolute;left:260px;top:94px;width:680px;font-size:14px;line-height:1.55;color:var(--dark)}
.seo-body p{margin-bottom:22px}
.seo .btn{position:absolute;left:528px;top:268px;width:144px;height:34px;font-size:11px}

/* footer */
.footer{top:3232px;height:296px;background:var(--ink);color:var(--white)}
.news-title{position:absolute;left:160px;top:60px;font-family:"Oswald",sans-serif;font-weight:600;font-size:22px;text-transform:uppercase}
.news-text{position:absolute;left:160px;top:92px;font-size:12px;color:#d7d7d7}
.news-form{position:absolute;left:600px;top:62px;width:436px;height:42px;background:var(--white);border-radius:4px;display:flex;align-items:center;padding-left:14px;font-size:12px;color:#999}
.news-form .btn{position:absolute;right:0;top:0;height:42px;width:112px;border-radius:4px;font-size:12px}
.foot-nav{position:absolute;left:160px;top:160px;display:flex;gap:48px;font-size:15px}
.foot-nav a{color:var(--white);text-decoration:none}
.foot-nav a.active{color:var(--orange)}
.socials{position:absolute;left:960px;top:162px;display:flex;gap:18px}
.socials i{width:16px;height:16px;border-radius:50%;background:var(--white)}
.foot-rule{position:absolute;left:160px;top:214px;width:880px;height:1px;background:#5a5a59}
.payments{position:absolute;left:0;width:1200px;top:244px;display:flex;justify-content:center;gap:12px}
.payments i{width:52px;height:30px;border-radius:4px;background:var(--white)}
</style>
</head>
<body>

<div class="section topbar">
  <svg width="14" height="14" viewBox="0 0 24 24" fill="#fff"><path d="M6.6 10.8a15 15 0 0 0 6.6 6.6l2.2-2.2c.3-.3.7-.4 1-.2 1.1.4 2.3.6 3.6.6.6 0 1 .4 1 1V20c0 .6-.4 1-1 1A17 17 0 0 1 3 4c0-.6.4-1 1-1h3.5c.6 0 1 .4 1 1 0 1.3.2 2.5.6 3.6.1.3 0 .7-.2 1z"/></svg>
  <span>Questions? 020 555 0192</span>
</div>

<header class="section header">
  <div class="logo"><span class="logo-dot"></span>brenvik</div>
  <div class="search">
    <svg width="14" height="14" viewBox="0 0 24 24" fill="none" stroke="#999" stroke-width="2.4"><circle cx="10" cy="10" r="7"/><path d="M15 15l6 6"/></svg>
    Search for...
  </div>
  <div class="account">
    <svg width="14" height="14" viewBox="0 0 24 24" fill="none" stroke="#3c3c3b" stroke-width="2"><circle cx="12" cy="8" r="4"/><path d="M4 21c1-4 4-6 8-6s7 2 8 6"/></svg>
    Account
  </div>
  <div class="cart">
    <svg width="15" height="15" viewBox="0 0 24 24" fill="none" stroke="#fff" stroke-width="2"><path d="M3 4h3l2 11h11l2-8H7"/><circle cx="9" cy="20" r="1.5"/><circle cx="18" cy="20" r="1.5"/></svg>
    $0.00
  </div>
</header>

<nav class="section nav">
  <a class="active" href="#">Home</a><a href="#">About</a><a href="#">Fishing</a><a href="#">Chickens</a><a href="#">Categories</a><a href="#">Contact Us</a>
</nav>

<section class="section hero">
  <div class="media hero-media" role="img" aria-label="Tropical fish swimming beside bags and tubs of fish food"></div>
  <h1 class="heading hero-title">Premium Hemp &amp;<br>THCA Products</h1>
  <p class="hero-text">Quality hemp products from trusted farms. Third-party tested for purity.</p>
  <span class="btn btn-dark">Shop Now</span>
  <div class="slide-arrow" style="left:0"><svg width="12" height="16" viewBox="0 0 12 16"><path d="M9 2L3 8l6 6" stroke="#fff" stroke-width="2.4" fill="none"/></svg></div>
  <div class="slide-arrow" style="right:0"><svg width="12" height="16" viewBox="0 0 12 16"><path d="M3 2l6 6-6 6" stroke="#fff" stroke-width="2.4" fill="none"/></svg></div>
</section>

<section class="section categories">
  <h2 class="heading section-title" style="top:36px">Categories</h2>
  <div class="cat-card" style="left:160px">
    <div class="cat-label"><span class="small">Fish</span><span class="big">Food</span></div>
    <div class="media cat-media" style="background:radial-gradient(circle,#f08a2c 0%,rgba(240,138,44,.2) 70%,rgba(255,255,255,0) 72%)" role="img" aria-label="Orange goldfish"></div>
  </div>
  <div class="cat-card" style="left:466px">
    <div class="cat-label"><span class="small">Chicken</span><span class="big">Food</span></div>
    <div class="media cat-media" style="background:radial-gradient(circle,#a4502a 0%,rgba(164,80,42,.25) 70%,rgba(255,255,255,0) 72%)" role="img" aria-label="Brown rooster"></div>
  </div>
  <div class="cat-card accent" style="left:772px">
    <div class="cat-label"><span class="small">Chicken</span><span class="big">Accessories</span></div>
    <div class="media cat-media" style="left:60px;top:100px;width:150px;height:170px;border-radius:10px;background:linear-gradient(180deg,#e9552f,#3a2b26)" role="img" aria-label="Tub of poultry supplement"></div>
  </div>
</section>

<section class="section featured">
  <h2 class="heading section-title" style="top:18px">Featured Products</h2>
  <div class="product" style="left:100px">
    <div class="stars">★★★★★ <span>(05)</span></div>
    <div class="media product-media" style="background:linear-gradient(180deg,#2b63b4,#e8c23a)" role="img" aria-label="Fish flake food tin"></div>
    <div class="price">$00.00</div>
    <div class="product-name">AquaMin Flake</div>
    <div class="add-cart">Add To Cart</div>
  </div>
  <div class="product" style="left:355px">
    <div class="stars">★★★★★ <span>(05)</span></div>
    <div class="media product-media" style="background:linear-gradient(180deg,#f2ede3,#e59a3a)" role="img" aria-label="Bag of chicken feed"></div>
    <div class="price">$00.00</div>
    <div class="product-name">Farmyard Chicken</div>
    <div class="add-cart">Add To Cart</div>
  </div>
  <div class="product" style="left:610px">
    <div class="stars">★★★★★ <span>(05)</span></div>
    <div class="media product-media" style="background:linear-gradient(180deg,#2f2f2f,#b8342b)" role="img" aria-label="Pouch of fish pellets"></div>
    <div class="price">$00.00</div>
    <div class="product-name">Skyline Basic</div>
    <div class="add-cart">Add To Cart</div>
  </div>
  <div class="product" style="left:865px">
    <div class="stars">★★★★★ <span>(05)</span></div>
    <div class="media product-media" style="background:linear-gradient(180deg,#9c5bd0,#f1e9f7)" role="img" aria-label="Pouch of arowana food"></div>
    <div class="price">$00.00</div>
    <div class="product-name">Prime Arowana</div>
    <div class="add-cart">Add To Cart</div>
  </div>
  <div class="dots"><i class="on"></i><i></i><i></i><i></i></div>
  <span class="btn btn-orange view-all">View All Products</span>
</section>

<section class="section deal">
  <div class="media deal-media" role="img" aria-label="Koi fish in splashing water beside fish food packs"></div>
  <h2 class="heading deal-title">Deal Of The Week</h2>
  <p class="deal-text">Quality fish food from trusted farms. Third-party tested for purity.</p>
  <span class="btn btn-orange">Shop Now</span>
</section>

<section class="section promos">
  <div class="promo" style="left:64px">
    <div class="promo-side"></div>
    <div class="media promo-media" style="background:linear-gradient(180deg,#3a3a36,#d8922f)" role="img" aria-label="Fish food packs"></div>
    <div class="promo-text"><span class="hl">Nutrition</span>For Growth<br>&amp; Colour.</div>
    <div class="promo-go"><svg width="12" height="12" viewBox="0 0 12 12"><path d="M2 6h8M6 2l4 4-4 4" stroke="#fff" stroke-width="1.8" fill="none"/></svg></div>
  </div>
  <div class="promo" style="left:428px">
    <div class="promo-side"></div>
    <div class="media promo-media" style="background:linear-gradient(180deg,#f3ece0,#b96a2c)" role="img" aria-label="Chicken feed bags"></div>
    <div class="promo-text"><span class="hl">Save Big</span>Shop Big</div>
    <div class="promo-go"><svg width="12" height="12" viewBox="0 0 12 12"><path d="M2 6h8M6 2l4 4-4 4" stroke="#fff" stroke-width="1.8" fill="none"/></svg></div>
  </div>
  <div class="promo" style="left:792px">
    <div class="promo-side"></div>
    <div class="media promo-media" style="background:linear-gradient(180deg,#8f5ac4,#e44a3a)" role="img" aria-label="Fish food pouches"></div>
    <div class="promo-text"><span class="hl">Save On</span>Final<br>Frights</div>
    <div class="promo-go"><svg width="12" height="12" viewBox="0 0 12 12"><path d="M2 6h8M6 2l4 4-4 4" stroke="#fff" stroke-width="1.8" fill="none"/></svg></div>
  </div>
</section>

<section class="section why">
  <svg class="ribbon" viewBox="0 0 704 304">
    <path d="M0 0H704V250L352 304L0 250Z" fill="#f7a441"/>
    <path d="M14 14H690V238L352 290L14 238Z" fill="none" stroke="#fff" stroke-width="2"/>
  </svg>
  <h2 class="heading why-title">Why Choose Us</h2>
  <p class="why-text">We're here to bring nature to animals that you have the best possible experience with the highest quality products.</p>
  <div class="usp" style="left:340px;top:176px">
    <svg width="38" height="28" viewBox="0 0 38 28" fill="#fff"><rect x="0" y="4" width="22" height="16" rx="2"/><path d="M23 9h8l6 6v5H23z"/><circle cx="8" cy="23" r="4"/><circle cx="29" cy="23" r="4"/></svg>
    Fast Delivery
  </div>
  <div class="usp" style="left:520px;top:150px">
    <svg width="30" height="34" viewBox="0 0 30 34" fill="#fff"><circle cx="15" cy="13" r="12"/><path d="M8 22l-3 11 10-5 10 5-3-11z"/><path d="M10 13l4 4 7-7" stroke="#f7a441" stroke-width="3" fill="none"/></svg>
    High-Quality Feed
  </div>
  <div class="usp" style="left:760px;top:170px">
    <svg width="32" height="34" viewBox="0 0 32 34" fill="#fff"><circle cx="16" cy="9" r="7"/><path d="M2 33c1-9 6-13 14-13s13 4 14 13z"/></svg>
    <span>Trusted By<br>Professionals</span>
  </div>
</section>

<section class="section seo">
  <h2 class="heading section-title seo-title">Lorem Ipsum</h2>
  <div class="seo-body">
    <p>Lorem Ipsum is simply dummy text of the printing and typesetting industry. Lorem Ipsum has been the industry's standard dummy text ever since the 1500s, when an unknown printer took a galley of type and scrambled it to make a type specimen book.</p>
    <p>Lorem Ipsum is simply dummy text of the printing and typesetting industry. Lorem Ipsum has been the industry's standard dummy text ever since the 1500s, when an unknown printer took a galley of type and scrambled it to make a type specimen book.</p>
  </div>
  <span class="btn btn-orange">Learn More</span>
</section>

<footer class="section footer">
  <div class="news-title">Sign Up For Our Newsletter</div>
  <div class="news-text">Keep your inbox stocked with new products, tips &amp; more.</div>
  <div class="news-form">Your Email Address<span class="btn btn-orange">Subscribe</span></div>
  <nav class="foot-nav">
    <a class="active" href="#">Home</a><a href="#">Fishing</a><a href="#">Chickens</a><a href="#">Categories</a><a href="#">Blog</a><a href="#">Contact Us</a>
  </nav>
  <div class="socials"><i></i><i></i><i></i></div>
  <div class="foot-rule"></div>
  <div class="payments"><i></i><i></i><i></i><i></i></div>
</footer>

</body>
</html>
```